Criminal Defense Law Firm needs Stationary design Theme for a Business Card, Envelope, and Letterhea

Our Law Firm is seeking a general design concept for a business card, letterhead, and Envelope.

Our website is WillowcrestTrialDesk.com

A design for these three items is requested to keep branding in place for the firm. Would like to keep the Firm Colors on the website consistent with our branding on business cards, letterheads, and mailing envelopes #10 size to be exact.

We would like business cards printed front and back with Law firm Colors from website.

Letterhead with law firm colors as well. Design is not limited to just the header, but the footer can be utilized as well for email, website, phone, fax, etc.

Simple #10 envelope consisting of the same design principles set out in the previous two designs.

```html
<!DOCTYPE html>
<html lang="en">
<head>
<meta charset="utf-8">
<title>Willowcrest Criminal Defense Offices – Stationery</title>
<link href="https://fonts.googleapis.com/css2?family=Cormorant+Garamond:wght@500&family=Open+Sans:wght@400;600;700&display=swap" rel="stylesheet">
<style>
:root{
  --ink:#2b2b2b;
  --paper:#ffffff;
  --backdrop:#ebebeb;
  --body:#555555;
  --accent:#3aa6d8;
}
*{box-sizing:border-box;margin:0;padding:0}
html,body{width:1200px;height:937px;overflow:hidden;background:var(--backdrop);font-family:"Open Sans",Arial,sans-serif;color:var(--ink)}
.sheet{position:absolute;background:var(--paper);overflow:hidden}
.band{position:absolute;left:0;right:0;bottom:0;background:var(--ink)}
.url-tab{position:absolute;right:0;background:var(--ink);color:#fff;border:2px solid var(--paper);border-right:none;border-radius:12px 0 0 0;font-weight:400;display:flex;align-items:center;justify-content:center;white-space:nowrap}
.brand{position:absolute;display:flex;align-items:center;font-family:"Cormorant Garamond",Georgia,serif;font-weight:500;color:var(--ink);text-transform:uppercase;letter-spacing:.04em;line-height:1.05}
.brand .dot{border:1.5px solid var(--ink);border-radius:50%;flex:none}

/* letterhead */
.letterhead{left:185px;top:68px;width:387px;height:544px}
.letterhead .brand{left:38px;top:28px;flex-direction:column;align-items:flex-start;font-size:12.5px}
.letterhead .brand .dot{width:28px;height:28px;margin:0 0 10px 42px}
.contact{position:absolute;font-size:7px;line-height:1.35;color:var(--body)}
.contact b{color:var(--ink);font-weight:700}
.contact .ico{display:inline-block;width:5px;height:5px;background:var(--accent);border-radius:50%;margin-right:4px;vertical-align:middle}
.letterhead .contact{left:265px;top:20px;font-size:7.5px}
.letter{position:absolute;left:36px;top:137px;width:300px;font-size:5.3px;line-height:1.5;color:var(--body)}
.letter p{margin-bottom:9px}
.letter .gap{margin-bottom:22px}
.signature{width:28px;height:22px;background:#d6d6d6;margin:6px 0 8px}
.letterhead .band{height:23px}
.letterhead .url-tab{bottom:6px;width:182px;height:26px;font-size:11.5px}

/* folder */
.folder{left:636px;top:40px;width:458px;height:577px}
.folder .brand{left:95px;top:228px;flex-direction:column;align-items:flex-start;font-size:21px}
.folder .brand .dot{width:44px;height:44px;margin:0 0 18px 4px}
.folder .band{height:28px}
.folder .url-tab{bottom:8px;width:224px;height:28px;font-size:13px}

/* business cards */
.card{width:177px;height:100px;border-radius:8px}
.card-front{left:45px;top:658px}
.card-back{left:45px;top:785px}
.card-front .person{position:absolute;left:8px;top:14px;font-size:5.5px;line-height:1.3}
.card-front .person b{display:block;font-size:6px}
.card-front .brand{left:101px;top:22px;flex-direction:column;align-items:flex-start;font-size:7px}
.card-front .brand .dot{width:13px;height:13px;margin:0 0 4px 20px}
.card-front .contact{left:8px;top:54px;font-size:5px;line-height:1.3}
.card-front .contact .ico{width:3px;height:3px;margin-right:2px}
.card-front .band{height:8px}
.card-front .url-tab{bottom:2px;width:84px;height:12px;font-size:5.5px;border-radius:6px 0 0 0;border-width:1px}
.card-back .brand{left:42px;top:42px;font-size:7.5px;gap:5px}
.card-back .brand .dot{width:14px;height:14px}

/* envelope front */
.envelope-front{left:265px;top:671px;width:431px;height:210px}
.envelope-front .brand{left:115px;top:90px;font-size:13px;gap:9px}
.envelope-front .brand .dot{width:30px;height:30px}
.envelope-front .band{height:20px}
.envelope-front .url-tab{bottom:5px;width:205px;height:26px;font-size:12px}

/* envelope back */
.envelope-back{left:737px;top:671px;width:432px;height:210px}
.envelope-back .flap{position:absolute;left:0;top:0;width:100%;height:72px;background:var(--ink);border-radius:0 0 48px 48px;color:#fff;font-size:18px;display:flex;align-items:center;justify-content:center}
</style>
</head>
<body>

<section class="sheet letterhead" aria-label="Letterhead">
  <div class="brand"><span class="dot"></span><span>Willowcrest Criminal<br>Defense Offices</span></div>
  <div class="contact">
    <b><span class="ico"></span>041.12th floor,Harbor Line<br>&nbsp;&nbsp;&nbsp;Road KLM</b><br>
    <span class="ico"></span>012 345 6789<br>
    <span class="ico"></span>012 345 6789<br>
    <span class="ico"></span>urname@email.com
  </div>
  <div class="letter">
    <p>July 2, 2012</p>
    <p><b>Dear CH,</b><br>Elm Court, Oak St., Country Name</p>
    <p>is simply dummy text of the printing and typesetting industry. Lorem Ipsum has been the industry's standard dummy text ever since the 1500s, when an unknown printer took a galley of type and scrambled it to make a type specimen book. It has survived not only five centuries, but also the leap into electronic typesetting, remaining essentially unchanged. It was popularised in the 1960s with the release of transfer sheets containing Lorem Ipsum passages, and more recently with desktop publishing software and layout tools including versions of Lorem Ipsum.</p>
    <p class="gap">is simply dummy text of the printing and typesetting industry. Lorem Ipsum has been the industry's standard dummy text ever since the 1500s, when an unknown printer took a galley of type and scrambled it to make</p>
    <p>is simply dummy text of the printing and typesetting industry. Lorem Ipsum has been the industry's standard dummy text ever since the 1500s, when an unknown printer took a galley of type and scrambled it to make a type specimen book. It has survived not only five centuries, but also the leap into electronic typesetting, remaining essentially unchanged. It was popularised in the 1960s with the release of transfer sheets containing Lorem Ipsum passages, and more recently with desktop publishing software and layout tools including versions of Lorem Ipsum.</p>
    <p style="margin-bottom:0">Best Regards,</p>
    <div class="signature" role="img" aria-label="Handwritten signature"></div>
    <p><b>Samuel Reyes</b><br>Director<br><br>Elm Court, Oak St., Country Name</p>
  </div>
  <div class="band"></div>
  <div class="url-tab">www.urwebsitename.com</div>
</section>

<section class="sheet folder" aria-label="Presentation folder">
  <div class="brand"><span class="dot"></span><span>Willowcrest Criminal<br>Defense Offices</span></div>
  <div class="band"></div>
  <div class="url-tab">www.urwebsitename.com</div>
</section>

<section class="sheet card card-front" aria-label="Business card front">
  <div class="person"><b>DANIEL HARTWELL</b>Managing Director</div>
  <div class="brand"><span class="dot"></span><span>Willowcrest Criminal<br>Defense Offices</span></div>
  <div class="contact">
    <b><span class="ico"></span>041.12th floor,Harbor Line<br>&nbsp;&nbsp;Road KLM</b><br>
    <span class="ico"></span>012 345 6789<br>
    <span class="ico"></span>012 345 6789<br>
    <span class="ico"></span>urname@email.com
  </div>
  <div class="band"></div>
  <div class="url-tab">www.urwebsitename.com</div>
</section>

<section class="sheet card card-back" aria-label="Business card back">
  <div class="brand"><span class="dot"></span><span>Willowcrest Criminal<br>Defense Offices</span></div>
</section>

<section class="sheet envelope-front" aria-label="Envelope front">
  <div class="brand"><span class="dot"></span><span>Willowcrest Criminal<br>Defense Offices</span></div>
  <div class="band"></div>
  <div class="url-tab">www.urwebsitename.com</div>
</section>

<section class="sheet envelope-back" aria-label="Envelope back">
  <div class="flap">www.urwebsitename.com</div>
</section>

</body>
</html>
```